Tolnar Social Media Banner

The objective of this campaign is to end up with a Banner Add to post in the content of our social media.

We are Tolnar, a business that is going to modify all the grocery shopping mechanism with a simple device. It works the following way. Our device is a bar-code scanner. Once installed in your home, you would scan your groceries trough and it will automatically create your shopping list. Once you decide you have all the items, you just click the “buy” button and you’ll receive your groceries home whenever you have selected. This way is like being in the grocery shop but from home. You’ll find a long video and short video attached to the project.

The objective is to create a Banner Add that simulates the SHORT video with icons. The goal is for the viewer to understand what our device do just by looking at the banner. We have thought about diving the banner into three frames: Scan, Buy and Receive. Although that is what we think is most understandable, let us know if you think otherwise.

For the Scan frame the viewer should be able to see clearly the scanning process of any grocery through our device. I attached a picture of how our device looks like. You could also look for more images googling “Tolnar”.

For the Buy frame there should be a mobile phone. The idea is that the viewer is able to recognize that the Buying process is through an App in your phone. The frame could be only a phone, it could also be a phone with the Tolnar app opened or even a phone with a “Buy” button. Further ideas for this icon will be more than welcome.

The Receive frame should be the easiest one of them all. It should be more than clear the meaning of the frame.

Between the frames, you could add some to enable to understand the whole process. There could be numbers (Example: 1. Scan, 2. Buy, 3. Receive), there could be a plus sign (Example: Scan + Buy = Receive), or there could also be arrows following the process. Again, ideas to this matter will be more than welcome.

Thank you and contact us for questions or more info.

- Long video: https://www.vidmarsh.example/watch?v=Qa7rLmPzE2d

- Short Video: https://www.vidmarsh.example/watch?v=Hn3xBtYcW9k

- Tolnar Device Picture: https://www.findlo.example/search?q=tolnar&img=1#r=Pq4sTz8wLm2A

- Tolnar Logo: https://www.findlo.example/search?q=tolnar&img=1#r=Vd6kGh1nRs9B

- Tolnar App: https://www.findlo.example/search?q=tolnar+app&img=1#r=Jw2cYe5uXo7C

Industry/Entity Type

Business

Requirements
Must have
• Hi again. I just uploaded an example of what we are looking for. Open the file Tolnar_Expositor. We would like the designs to adjust to it. Although that's what we would like, we are open to new propositions.
• IMPORTANT:
• 1. We would like to change where it says scan. I've uploaded a picture called Captura. The idea is to draw the device SCANNING a product so that it is clear the function of the scan.
• 2. Dimensions of the composition. We would like more room for the Scan, Check and Receive compositions. That is going to be done reducing the blue space.
• 3. Bottom of the image. As you will see there is a pretty big grey space at the bottom of the image. The idea is to reduce it a little bit. The corner of the white line should be pretty close to the end of the image, or even touching.

```html
<!DOCTYPE html>
<html lang="en">
<head>
<meta charset="utf-8">
<title>Tolnar Social Media Banner</title>
<link href="https://fonts.googleapis.com/css2?family=Oswald:wght@300;500&display=swap" rel="stylesheet">
<style>
  :root {
    --grey-bg: #e2e2e4;
    --white: #ffffff;
    --blue: #36a3dc;
    --yellow: #fbbf14;
    --green: #8bc34a;
    --orange: #f0572a;
    --ink: #4d4d4d;
    --device: #d5d0c6;
  }
  html, body {
    margin: 0;
    padding: 0;
    width: 909px;
    height: 1200px;
    overflow: hidden;
    background: var(--grey-bg);
  }
  .banner {
    display: block;
    width: 909px;
    height: 1200px;
  }
  .bg { fill: var(--grey-bg); }
  .band-white { fill: var(--white); }
  .band-blue { fill: var(--blue); }
  .step-drop { stroke: var(--blue); stroke-width: 7; }
  .step-scan { fill: var(--yellow); }
  .step-buy { fill: var(--green); }
  .step-receive { fill: var(--orange); }
  .hero-drop { fill: var(--blue); stroke: var(--white); stroke-width: 54; stroke-linejoin: miter; }
  .step-number, .step-label, .hero-line {
    font-family: "Oswald", sans-serif;
    font-weight: 300;
    fill: var(--white);
  }
  .step-number { font-size: 76px; }
  .step-label { font-size: 58px; }
  .brand-mark {
    font-family: "Oswald", sans-serif;
    font-weight: 500;
    fill: var(--ink);
    font-size: 250px;
  }
  .brand-mark-small {
    font-family: "Oswald", sans-serif;
    font-weight: 500;
    fill: var(--white);
    font-size: 100px;
  }
  .brand-square { fill: var(--blue); }
  .brand-square-small { fill: var(--orange); }
  .hero-line-lg { font-size: 96px; }
  .hero-line-md { font-size: 60px; }
  .hero-line-sm { font-size: 56px; }
  .device-shot { fill: var(--device); }
  .phone-shot { fill: #eeeeee; }
  .groceries-shot { fill: #c9a98e; }
  .device-glow { fill: #ffffff; opacity: 0.35; }
</style>
</head>
<body>
<svg class="banner" viewBox="0 0 1136 1500" xmlns="http://www.w3.org/2000/svg">
  <rect class="bg" x="0" y="0" width="1136" height="1500"/>

  <!-- white diagonal band -->
  <polygon class="band-white" points="70,0 1116,960 1116,1412 0,1075 0,0"/>

  <!-- blue step strips -->
  <polygon class="band-blue" points="0,18 230,190 230,380 0,318"/>
  <polygon class="band-blue" points="0,345 230,515 230,700 0,648"/>
  <polygon class="band-blue" points="0,672 230,842 230,1030 0,975"/>

  <!-- step 1: scan -->
  <g class="step">
    <text class="step-number" x="48" y="166">1</text>
    <path class="step-drop step-scan" d="M36,292 A124,124 0 0 1 284,292 L284,416 L160,416 A124,124 0 0 1 36,292 Z"/>
    <rect class="device-shot" x="132" y="215" width="52" height="92" rx="6" role="img" aria-label="Tolnar scanner device"/>
    <text class="step-label" x="160" y="372" text-anchor="middle">Scan</text>
  </g>

  <!-- step 2: buy -->
  <g class="step">
    <text class="step-number" x="45" y="494">2</text>
    <path class="step-drop step-buy" d="M41,617 A124,124 0 0 1 289,617 L289,741 L165,741 A124,124 0 0 1 41,617 Z"/>
    <rect class="phone-shot" x="135" y="540" width="55" height="110" rx="8" role="img" aria-label="Phone showing the Tolnar app"/>
    <text class="step-label" x="165" y="707" text-anchor="middle">Buy</text>
  </g>

  <!-- step 3: receive -->
  <g class="step">
    <text class="step-number" x="45" y="816">3</text>
    <path class="step-drop step-receive" d="M38,945 A124,124 0 0 1 286,945 L286,1069 L162,1069 A124,124 0 0 1 38,945 Z"/>
    <rect class="groceries-shot" x="110" y="880" width="112" height="76" rx="8" role="img" aria-label="Delivered grocery products"/>
    <text class="step-label" x="167" y="1016" text-anchor="middle">Receive</text>
  </g>

  <!-- top brand -->
  <rect class="brand-square" x="700" y="80" width="24" height="24"/>
  <text class="brand-mark" x="505" y="262" textLength="595" lengthAdjust="spacingAndGlyphs">tolnar</text>

  <!-- hero -->
  <path class="hero-drop" d="M305,995 A390,390 0 0 1 1088,995 L1088,1385 L695,1385 A390,390 0 0 1 305,995 Z"/>
  <path class="hero-drop" style="stroke:none" d="M305,995 A390,390 0 0 1 1088,995 L1088,1385 L695,1385 A390,390 0 0 1 305,995 Z"/>

  <rect class="brand-square-small" x="565" y="823" width="11" height="11"/>
  <text class="brand-mark-small" x="478" y="902" textLength="258" lengthAdjust="spacingAndGlyphs">tolnar</text>
  <text class="hero-line hero-line-lg" x="731" y="1034" text-anchor="end">Does Your</text>
  <text class="hero-line hero-line-md" x="722" y="1106" text-anchor="end">Grocery Shopping</text>
  <text class="hero-line hero-line-sm" x="731" y="1175" text-anchor="end">for you ?</text>

  <rect class="device-glow" x="770" y="835" width="215" height="375" rx="22"/>
  <rect class="device-shot" x="782" y="845" width="192" height="352" rx="14" role="img" aria-label="Tolnar scanner device, front view"/>
</svg>
</body>
</html>
```